Harwell Construct, LLC Business Card
Business Car Design
Harwell Construct, LLC Business Card - Construction
Creative Brief
Professional
Tom Morrow
Owner
P.O. Box 5817 Marlow Creek, GA 30521
tmorrow@harwellconstructsc.example
www.harwellconstructsc.example
Back of Business Card should be just the logo that fills up the page.

```html
<!DOCTYPE html>
<html lang="en">
<head>
<meta charset="utf-8">
<title>Harwell Construct, LLC Business Card</title>
<link rel="stylesheet" href="https://fonts.googleapis.com/css2?family=Libre+Caslon+Text:wght@400;700&display=swap">
<style>
  :root {
    --stage: #2e2e2e;
    --card: #ffffff;
    --card-shade: #f1f1f0;
    --brand-brown: #4a3222;
    --ink: #2a2a2a;
    --ink-soft: #555555;
    --ghost: #e4e4e2;
  }
  html, body {
    margin: 0;
    padding: 0;
    width: 1200px;
    height: 780px;
    overflow: hidden;
    background: var(--stage);
    font-family: "Libre Caslon Text", Georgia, serif;
  }
  .business-card {
    position: absolute;
    left: 100px;
    top: 105px;
    width: 1000px;
    height: 570px;
    background: linear-gradient(135deg, var(--card) 55%, var(--card-shade) 100%);
    border-radius: 34px;
    overflow: hidden;
  }
  .edge-tab {
    position: absolute;
    left: 0;
    top: 400px;
    width: 12px;
    height: 110px;
    background: var(--brand-brown);
  }
  .brand-decoration {
    position: absolute;
    left: 520px;
    top: -40px;
    width: 520px;
    height: 560px;
    border-radius: 48% 52% 40% 60%;
    background: radial-gradient(ellipse at 50% 45%, var(--ghost) 0%, rgba(228,228,226,0.6) 55%, rgba(255,255,255,0) 74%);
  }
  .brand-block {
    position: absolute;
    left: 80px;
    top: 90px;
    width: 380px;
    display: flex;
    align-items: center;
    gap: 14px;
  }
  .brand-square {
    width: 28px;
    height: 28px;
    background: var(--brand-brown);
    flex: none;
  }
  .brand-name {
    margin: 0;
    font-size: 36px;
    font-weight: 400;
    color: var(--brand-brown);
    letter-spacing: 0.5px;
    white-space: nowrap;
  }
  .brand-rule {
    position: absolute;
    left: 80px;
    top: 160px;
    width: 380px;
    height: 2px;
    background: var(--brand-brown);
  }
  .person {
    position: absolute;
    left: 620px;
    top: 300px;
    width: 280px;
    text-align: center;
  }
  .person-name {
    margin: 0;
    font-size: 28px;
    font-weight: 700;
    color: var(--ink);
  }
  .person-title {
    margin: 6px 0 0;
    font-size: 19px;
    color: var(--ink-soft);
  }
  .contact-address {
    position: absolute;
    left: 80px;
    top: 290px;
    margin: 0;
    font-size: 18px;
    color: var(--ink);
    white-space: nowrap;
  }
  .contact-list {
    position: absolute;
    left: 80px;
    top: 340px;
    margin: 0;
    padding: 0;
    list-style: none;
    font-size: 18px;
    color: var(--ink);
  }
  .contact-list li {
    display: flex;
    align-items: center;
    gap: 10px;
    height: 34px;
    white-space: nowrap;
  }
  .contact-list svg {
    width: 19px;
    height: 19px;
    flex: none;
  }
  .phone-pair {
    display: flex;
    align-items: center;
    gap: 10px;
  }
</style>
</head>
<body>
  <article class="business-card">
    <div class="edge-tab"></div>
    <div class="brand-decoration" role="img" aria-label="Faint large brand backdrop"></div>

    <header class="brand-block">
      <div class="brand-square"></div>
      <h1 class="brand-name">Harwell Construct</h1>
    </header>
    <div class="brand-rule"></div>

    <section class="person">
      <p class="person-name">Tom Morrow</p>
      <p class="person-title">Owner</p>
    </section>

    <p class="contact-address">P.O. Box 5817 Marlow Creek, GA 30521</p>

    <ul class="contact-list">
      <li>
        <span class="phone-pair">
          <svg viewBox="0 0 24 24" aria-hidden="true"><path fill="#2a2a2a" d="M6.6 10.8a15.1 15.1 0 0 0 6.6 6.6l2.2-2.2c.3-.3.7-.4 1-.2 1.1.4 2.3.6 3.6.6.6 0 1 .4 1 1V20c0 .6-.4 1-1 1C10.6 21 3 13.4 3 4c0-.6.4-1 1-1h3.5c.6 0 1 .4 1 1 0 1.3.2 2.5.6 3.6.1.3 0 .7-.2 1z"/></svg>
          <span>555-201-4417</span>
          <svg viewBox="0 0 24 24" aria-hidden="true"><rect x="7" y="2" width="10" height="20" rx="2" fill="#2a2a2a"/><rect x="9" y="5" width="6" height="11" fill="#ffffff"/><circle cx="12" cy="19" r="1.2" fill="#ffffff"/></svg>
          <span>555-388-0926</span>
        </span>
      </li>
      <li>
        <svg viewBox="0 0 24 24" aria-hidden="true"><circle cx="12" cy="12" r="11" fill="#2a2a2a"/><text x="12" y="16.5" text-anchor="middle" font-size="13" font-family="Georgia, serif" fill="#ffffff">@</text></svg>
        <span>tmorrow@harwellconstructsc.example</span>
      </li>
      <li>
        <svg viewBox="0 0 24 24" aria-hidden="true"><circle cx="12" cy="12" r="10" fill="none" stroke="#2a2a2a" stroke-width="2"/><ellipse cx="12" cy="12" rx="4.5" ry="10" fill="none" stroke="#2a2a2a" stroke-width="1.6"/><line x1="2" y1="12" x2="22" y2="12" stroke="#2a2a2a" stroke-width="1.6"/></svg>
        <span>www.harwellconstructsc.example</span>
      </li>
    </ul>
  </article>
</body>
</html>
```